Business Recognition Design

We need a design for a recognition to be given to business leaders in our community.
The recognition shall be made on a brass plaque on wood panel background (picture attached, please use it as a background), and all drawing must be in vectors and only one color (black).
It should also have a logo on the top and signature on the right bottom.
The text is enclosed in DOC file.

Reason: just to be able to find the best solution

Reason: None of the suggestion is good enough. Logo in general is too big in comparison with the rest of the plate.

Industry/Entity Type

Business

Requirements
Must have
• - standard Windows font (or possibility to install the same font on Windows), as the name on the recognition shall be printed in the same font
Nice to have
• - some graphic element (in curves) representing achievements in business
- should look great :)

```html
<!DOCTYPE html>
<html lang="de">
<head>
<meta charset="utf-8">
<title>Auszeichnung – Kapitalwerk</title>
<link rel="stylesheet" href="https://fonts.googleapis.com/css2?family=Arimo:wght@400;700&family=Italianno&display=swap">
<style>
  :root {
    --wood-dark: #3e2614;
    --wood-mid: #6b4429;
    --wood-light: #8a5d3b;
    --brass-deep: #b88f2a;
    --brass-mid: #d9b245;
    --brass-light: #f6dc7a;
    --brass-edge: #9c7620;
    --ink: #111111;
    --screw-dark: #6e5210;
    --screw-light: #f1d36a;
  }
  html, body {
    margin: 0;
    padding: 0;
    width: 1200px;
    height: 924px;
    overflow: hidden;
    background: #ffffff;
  }
  .plaque-board {
    position: relative;
    width: 1200px;
    height: 924px;
    background:
      repeating-linear-gradient(95deg, rgba(0,0,0,0.08) 0 3px, rgba(255,255,255,0.03) 3px 7px),
      linear-gradient(135deg, var(--wood-mid), var(--wood-dark) 45%, var(--wood-light) 70%, var(--wood-dark));
    box-shadow: inset 0 0 0 4px rgba(0,0,0,0.35), inset 0 0 24px rgba(0,0,0,0.6);
    font-family: "Arimo", Arial, sans-serif;
    color: var(--ink);
  }
  .brass-plate {
    position: absolute;
    left: 55px;
    top: 49px;
    width: 1093px;
    height: 824px;
    background:
      repeating-linear-gradient(0deg, rgba(255,255,255,0.06) 0 1px, rgba(0,0,0,0.04) 1px 3px),
      linear-gradient(100deg, var(--brass-deep), var(--brass-light) 22%, var(--brass-mid) 40%, var(--brass-light) 62%, var(--brass-mid) 80%, var(--brass-deep));
    border: 3px solid var(--brass-edge);
    box-shadow: 0 0 0 2px rgba(255,240,180,0.5) inset, 3px 4px 10px rgba(0,0,0,0.55);
    box-sizing: border-box;
  }
  .screw {
    position: absolute;
    width: 28px;
    height: 28px;
    border-radius: 50%;
    background: radial-gradient(circle at 40% 38%, var(--screw-light), var(--brass-mid) 45%, var(--screw-dark));
    box-shadow: 0 0 0 2px rgba(80,55,10,0.6), 1px 2px 3px rgba(0,0,0,0.5);
  }
  .screw--tl { left: 62px; top: 71px; }
  .screw--tr { left: 1093px; top: 71px; }
  .screw--bl { left: 62px; top: 824px; }
  .screw--br { left: 1093px; top: 824px; }

  .brand-name {
    position: absolute;
    left: 0;
    width: 1200px;
    top: 142px;
    text-align: center;
    font-weight: 700;
    font-size: 40px;
    letter-spacing: -0.5px;
  }
  .ornament-band {
    position: absolute;
    left: 158px;
    top: 207px;
    width: 884px;
    height: 142px;
  }
  .award-title {
    position: absolute;
    left: 0;
    width: 1200px;
    top: 362px;
    text-align: center;
    font-size: 52px;
    line-height: 1;
    letter-spacing: 0.5px;
  }
  .award-reason {
    position: absolute;
    left: 0;
    width: 1200px;
    top: 451px;
    text-align: center;
    font-size: 30px;
    line-height: 1;
  }
  .award-for {
    position: absolute;
    left: 0;
    width: 1200px;
    top: 498px;
    text-align: center;
    font-size: 23px;
    line-height: 1;
  }
  .recipient-name {
    position: absolute;
    left: 0;
    width: 1200px;
    top: 542px;
    text-align: center;
    font-size: 38px;
    line-height: 1;
  }
  .citation {
    position: absolute;
    left: 0;
    width: 1200px;
    top: 599px;
    margin: 0;
    text-align: center;
    font-size: 20.5px;
    line-height: 36px;
  }
  .place-date {
    position: absolute;
    left: 144px;
    top: 768px;
    font-size: 23px;
    line-height: 1;
  }
  .signatory {
    position: absolute;
    right: 150px;
    top: 758px;
    font-family: "Italianno", cursive;
    font-size: 44px;
    line-height: 1;
  }
</style>
</head>
<body>
  <main class="plaque-board">
    <div class="brass-plate"></div>
    <span class="screw screw--tl"></span>
    <span class="screw screw--tr"></span>
    <span class="screw screw--bl"></span>
    <span class="screw screw--br"></span>

    <div class="brand-name">Kapitalwerk</div>

    <svg class="ornament-band" viewBox="0 0 884 142" role="img" aria-label="Ornamentale Zierleiste aus geschwungenen Linien und Rauten">
      <defs>
        <linearGradient id="ornament-fade" x1="0" x2="1" y1="0" y2="0">
          <stop offset="0" stop-color="#1a1408" stop-opacity="0"/>
          <stop offset="0.5" stop-color="#1a1408" stop-opacity="0.28"/>
          <stop offset="1" stop-color="#1a1408" stop-opacity="0"/>
        </linearGradient>
      </defs>
      <rect x="0" y="36" width="884" height="70" rx="35" fill="url(#ornament-fade)"/>
    </svg>

    <h1 class="award-title" style="margin:0;font-weight:400;">AUSZEICHNUNG</h1>
    <div class="award-reason">als herausragendster Unternehmer Deutschlands 2013</div>
    <div class="award-for">für</div>
    <div class="recipient-name">Herrn Dipl.–Kfm. Max Muster</div>
    <p class="citation">
      Unter der Leitung von Herr Dipl.–Kfm. Max Muster<br>
      hat sich die FIRMA GmbH im Jahr 2013 unter<br>
      den ersten 5% der größten deutschen Wirtschaftsunternehmen platziert.
    </p>

    <div class="place-date">Gilching, 20. Juni 2013</div>
    <div class="signatory">Helena Brandt</div>
  </main>
</body>
</html>
```